Postcard Design

Law office.
Details are on the attached pdf file:
NOTE: the following items are to be changed, as follows:
1. price is 799
2. delete "Expires 2-8-13"
3. make "Nevada County's..." into "Northern California's ... "
4. Someplace where it fits nicely, add "Fast, Easy, Done!"
5. Delete "no obligation first visit"
6. That attached pdf was a successful ad so I want to maintain that look GENERALLY, but I'm not stuck on anything in particular. Some freedom to play with it for a perfect ad.
7. I'll attach the revised picture and the logo.

```html
<!DOCTYPE html>
<html lang="en">
<head>
<meta charset="utf-8">
<title>Law Office of Daniel R. Moretti – Estate Plans Postcard</title>
<link rel="stylesheet" href="https://fonts.googleapis.com/css2?family=Cormorant+Garamond:wght@400;500;700&display=swap">
<style>
  :root {
    --ink: #111111;
    --paper-light: #ffffff;
    --paper-blue: #c9e6f8;
    --frame: #0d0d0d;
    --photo-top: #8e9398;
    --photo-bottom: #3b3f44;
    --photo-mat: #ffffff;
  }
  html, body {
    margin: 0;
    padding: 0;
    overflow: hidden;
    background: #ffffff;
  }
  .postcard {
    position: relative;
    width: 1200px;
    height: 863px;
    overflow: hidden;
    background: linear-gradient(100deg, var(--paper-light) 0%, #eef7fd 45%, var(--paper-blue) 100%);
    font-family: "Cormorant Garamond", Georgia, serif;
    color: var(--ink);
  }
  .border-frame {
    position: absolute;
    left: 30px; top: 28px;
    width: 1136px; height: 804px;
    border: 4px solid var(--frame);
  }
  .text {
    position: absolute;
    margin: 0;
    white-space: nowrap;
    line-height: 1;
  }
  .headline {
    left: 0; right: 0; top: 62px;
    text-align: center;
    font-size: 52px;
    font-weight: 700;
  }
  .subhead {
    left: 0; right: 0; top: 126px;
    text-align: center;
    font-size: 50px;
    font-weight: 500;
  }
  .price {
    left: 232px; top: 218px;
    font-size: 140px;
    font-weight: 500;
  }
  .price-note {
    left: 622px; top: 262px;
    font-size: 18px;
    font-weight: 500;
  }
  .price-value {
    left: 622px; top: 288px;
    font-size: 32px;
    font-weight: 700;
  }
  .tagline {
    left: 0; right: 0; top: 390px;
    padding-left: 20px;
    text-align: center;
    font-size: 58px;
    font-weight: 500;
  }
  .promise {
    left: 428px; top: 482px;
    font-size: 26px;
    font-weight: 700;
  }
  .office-label {
    left: 420px; top: 540px;
    font-size: 32px;
    font-weight: 500;
  }
  .attorney-name {
    left: 250px; top: 588px;
    width: 730px;
    text-align: center;
    font-size: 84px;
    font-weight: 500;
  }
  .phone {
    left: 440px; top: 690px;
    width: 400px;
    text-align: center;
    font-size: 46px;
    font-weight: 500;
  }
  .website {
    left: 440px; top: 748px;
    width: 400px;
    text-align: center;
    font-size: 25px;
    font-weight: 700;
  }
  .notary {
    left: 440px; top: 790px;
    width: 400px;
    text-align: center;
    font-size: 22px;
    font-weight: 500;
  }
  .portrait-frame {
    position: absolute;
    left: 38px; top: 528px;
    width: 196px; height: 278px;
    background: var(--photo-mat);
    border: 1px solid #9a9a9a;
    box-sizing: border-box;
  }
  .portrait {
    position: absolute;
    left: 8px; top: 8px; right: 8px; bottom: 8px;
    background: linear-gradient(180deg, var(--photo-top) 0%, #6a6f74 55%, var(--photo-bottom) 100%);
    border: 2px solid var(--ink);
  }
  .brand-mark {
    position: absolute;
    left: 1014px; top: 573px;
    width: 126px; height: 155px;
    background: var(--photo-mat);
    border: 1px solid var(--ink);
    box-sizing: border-box;
    display: flex;
    align-items: center;
    justify-content: center;
  }
  .brand-mark-inner {
    width: 112px; height: 141px;
    border: 3px solid var(--ink);
    box-sizing: border-box;
    display: flex;
    align-items: center;
    justify-content: center;
    text-align: center;
    font-size: 24px;
    font-weight: 500;
    line-height: 1.1;
  }
  .since {
    left: 968px; top: 758px;
    width: 200px;
    text-align: center;
    font-size: 23px;
    font-weight: 500;
    line-height: 1.45;
    white-space: normal;
  }
</style>
</head>
<body>
  <main class="postcard">
    <div class="border-frame"></div>

    <h1 class="text headline">Northern California's Best in Estate Plans</h1>
    <p class="text subhead">Living Trusts, Wills &amp; All Necessary Documents</p>

    <p class="text price">$799</p>
    <p class="text price-note">Complete Estate Plan</p>
    <p class="text price-value">OVER $2,500 VALUE</p>

    <p class="text tagline">Peace of Mind for Your Family</p>
    <p class="text promise">FAST, EASY, DONE!</p>

    <p class="text office-label">Law Office Of</p>
    <p class="text attorney-name">Daniel R. Moretti</p>
    <p class="text phone">916-555-0142</p>
    <p class="text website">www.DanielMoretti.com</p>
    <p class="text notary">Free Notarization</p>

    <div class="portrait-frame">
      <div class="portrait" role="img" aria-label="Portrait photo of the attorney in a dark suit and tie"></div>
    </div>

    <div class="brand-mark">
      <div class="brand-mark-inner">Moretti<br>Law</div>
    </div>

    <p class="text since">Thousands Served<br>Since 1998</p>
  </main>
</body>
</html>
```